Online video and marketing company business cards

Need to get some new business cards designed to fit with our new logo. The cards should be professional, clean and simple.

Cards should have:

Name
Position
2 line address
telephone
mobile
email address
web address

We need to have our logo and if possible say what we do...
ONLINE FILM PRODUCTION & STRATEGY

Marketing

```html
<!DOCTYPE html>
<html lang="en">
<head>
<meta charset="utf-8">
<title>lumenreel business cards</title>
<link rel="stylesheet" href="https://fonts.googleapis.com/css2?family=Open+Sans:wght@400;600;700&display=swap">
<style>
  :root {
    --navy: #0e4a78;
    --sky: #6aa5c4;
    --sky-light: #8dbcd4;
    --ink: #2f3a44;
    --paper: #ffffff;
    --backdrop: #e9ecef;
  }
  * { box-sizing: border-box; margin: 0; padding: 0; }
  html, body { width: 1200px; height: 720px; overflow: hidden; }
  body {
    background: var(--backdrop);
    font-family: "Open Sans", Arial, sans-serif;
    position: relative;
  }
  .card {
    position: absolute;
    top: 205px;
    width: 540px;
    height: 309px;
    overflow: hidden;
    box-shadow: 0 6px 18px rgba(0,0,0,0.18);
  }
  .card--front { left: 40px; background: var(--paper); }
  .card--back { left: 620px; background: var(--sky); color: var(--paper); text-align: center; }

  .card__waves { position: absolute; inset: 0; width: 100%; height: 100%; }

  .brand {
    position: absolute;
    top: 38px;
    left: 44px;
    display: flex;
    align-items: center;
    gap: 10px;
  }
  .brand__dot {
    width: 30px; height: 30px;
    border-radius: 50%;
    background: var(--sky);
  }
  .brand__name {
    font-weight: 700;
    font-size: 44px;
    line-height: 1;
    color: var(--navy);
    letter-spacing: -0.5px;
  }

  .contact {
    position: absolute;
    top: 118px;
    left: 48px;
    list-style: none;
    font-size: 13px;
    color: var(--ink);
    line-height: 18px;
  }
  .contact__item { display: flex; align-items: center; gap: 7px; }
  .contact__icon { width: 11px; height: 11px; flex: none; }
  .contact__address { margin-top: 8px; padding-left: 18px; }

  .person {
    position: absolute;
    right: 26px;
    top: 148px;
    text-align: right;
    color: var(--paper);
  }
  .person__name { font-weight: 700; font-size: 17px; line-height: 1.2; }
  .person__title { font-size: 12px; }

  .back__brand {
    position: absolute;
    top: 82px;
    left: 0; right: 0;
    display: flex;
    justify-content: center;
    align-items: center;
    gap: 12px;
  }
  .back__dot { width: 38px; height: 38px; border-radius: 50%; background: var(--paper); }
  .back__name { font-weight: 700; font-size: 50px; line-height: 1; }
  .back__tagline {
    position: absolute;
    top: 198px; left: 0; right: 0;
    font-size: 15px;
    letter-spacing: 2px;
  }
  .back__web {
    position: absolute;
    top: 232px; left: 0; right: 0;
    font-size: 16px;
    letter-spacing: 4px;
  }
</style>
</head>
<body>

<section class="card card--front" aria-label="Card front">
  <svg class="card__waves" viewBox="0 0 540 309" preserveAspectRatio="none" aria-hidden="true">
    <path d="M0,262 C150,292 300,222 380,140 C430,92 490,72 540,66" fill="none" stroke="var(--sky)" stroke-width="7"/>
    <path d="M0,276 C150,306 300,236 385,152 C435,104 490,86 540,82 L540,309 L0,309 Z" fill="var(--navy)"/>
    <path d="M0,296 C140,320 280,270 360,220" fill="none" stroke="var(--sky)" stroke-width="8"/>
    <path d="M380,180 C430,140 490,110 540,102" fill="none" stroke="var(--sky-light)" stroke-width="3"/>
  </svg>

  <div class="brand">
    <span class="brand__dot"></span>
    <span class="brand__name">lumenreel</span>
  </div>

  <ul class="contact">
    <li class="contact__item">
      <svg class="contact__icon" viewBox="0 0 12 12"><circle cx="6" cy="6" r="6" fill="var(--ink)"/><path d="M4 3.2 L5 4.8 L4.4 5.4 Q5.2 7 6.6 7.6 L7.2 7 L8.8 8 L8 9 Q4 8.4 3 4 Z" fill="var(--paper)"/></svg>
      123-456-0789
    </li>
    <li class="contact__item">
      <svg class="contact__icon" viewBox="0 0 12 12"><circle cx="6" cy="6" r="6" fill="var(--ink)"/><rect x="4.2" y="2.5" width="3.6" height="7" rx="0.6" fill="var(--paper)"/></svg>
      123-456-0789
    </li>
    <li class="contact__item">
      <svg class="contact__icon" viewBox="0 0 12 12"><circle cx="6" cy="6" r="6" fill="var(--ink)"/><rect x="3" y="4" width="6" height="4.2" fill="var(--paper)"/><path d="M3 4 L6 6.4 L9 4" fill="none" stroke="var(--ink)" stroke-width="0.8"/></svg>
      info@lumenreel.com
    </li>
    <li class="contact__item">
      <svg class="contact__icon" viewBox="0 0 12 12"><circle cx="6" cy="6" r="6" fill="var(--ink)"/><circle cx="6" cy="6" r="3.4" fill="none" stroke="var(--paper)" stroke-width="0.8"/><path d="M2.6 6 H9.4 M6 2.6 V9.4" stroke="var(--paper)" stroke-width="0.8"/></svg>
      www.lumenreel.com
    </li>
    <li class="contact__address">Street Name, City Name<br>State Zip Code</li>
  </ul>

  <div class="person">
    <p class="person__name">Your Name</p>
    <p class="person__title">Title</p>
  </div>
</section>

<section class="card card--back" aria-label="Card back">
  <div class="back__brand">
    <span class="back__dot"></span>
    <span class="back__name">lumenreel</span>
  </div>
  <p class="back__tagline">ONLINE FILM PRODUCTION &amp; STRATEGY</p>
  <p class="back__web">www.lumenreel.com</p>
</section>

</body>
</html>
```